Updated DJ business Card showing other businesses

DJ Kestro offers professional mobile dj services including DJ. MC. Karaoke.
Silent Disco (will attach logo)
I also offer a 360 Photo Booth.

Contact info:
(555) 314-7720
lenny.corbitt@mailvane.net
Social Media @DJKestroBPZ

```html
<!DOCTYPE html>
<html lang="en">
<head>
<meta charset="utf-8">
<title>DJ Kestro – Business Card</title>
<link href="https://fonts.googleapis.com/css2?family=Montserrat:wght@400;500;800&display=swap" rel="stylesheet">
<style>
  :root {
    --backdrop: #999999;
    --card-dark: #111111;
    --card-light: #ffffff;
    --ink: #111111;
    --accent: #d81e4a;
    --white: #ffffff;
  }
  * { margin: 0; padding: 0; box-sizing: border-box; }
  html, body { width: 1200px; height: 1000px; overflow: hidden; }
  body {
    background: var(--backdrop);
    font-family: "Montserrat", sans-serif;
    color: var(--ink);
    position: relative;
  }
  .card {
    position: absolute;
    left: 293px;
    width: 615px;
    height: 350px;
    border-radius: 32px;
    overflow: hidden;
  }
  .card--front { top: 123px; background: var(--card-dark); }
  .card--back { top: 540px; background: var(--card-light); }

  .brand {
    position: absolute;
    display: flex;
    align-items: center;
    gap: 14px;
    font-weight: 800;
    text-transform: uppercase;
    letter-spacing: 1px;
    white-space: nowrap;
  }
  .brand__dot { border-radius: 50%; background: var(--accent); flex: none; }
  .brand--front {
    left: 0; right: 0; top: 128px;
    justify-content: center;
    font-size: 66px; line-height: 80px;
    color: var(--white);
  }
  .brand--front .brand__dot { width: 40px; height: 40px; }
  .brand--back {
    left: 0; right: 0; top: 38px;
    justify-content: center;
    font-size: 40px; line-height: 52px;
    color: var(--accent);
  }
  .brand--back .brand__dot { width: 24px; height: 24px; background: var(--ink); }

  .tagline {
    position: absolute; left: 0; right: 0; top: 122px;
    text-align: center; font-size: 17px; font-weight: 500;
  }
  .services {
    position: absolute; left: 91px; top: 160px;
    list-style: none; font-size: 18px; font-weight: 500; line-height: 22px;
  }
  .services li::before { content: "• "; }

  .partner {
    position: absolute; left: 352px; top: 178px;
    display: flex; align-items: center; gap: 10px;
    font-size: 22px; font-weight: 800; text-transform: uppercase;
    white-space: nowrap;
  }
  .partner__dot { width: 28px; height: 28px; border-radius: 50%; background: var(--ink); }

  .contact {
    position: absolute; left: 93px; top: 271px;
    list-style: none; font-size: 18px; font-weight: 500;
  }
  .contact li { display: flex; align-items: center; gap: 8px; height: 28px; }
  .contact svg { width: 25px; height: 25px; flex: none; }

  .social {
    position: absolute; left: 384px; top: 267px; width: 150px;
    display: flex; flex-direction: column; align-items: center; gap: 6px;
  }
  .social__icons { display: flex; gap: 4px; }
  .social__icons span { width: 27px; height: 27px; border-radius: 50%; background: var(--accent); }
  .social__handle { font-size: 18px; font-weight: 500; }
</style>
</head>
<body>

<section class="card card--front" aria-label="Card front">
  <div class="brand brand--front"><span class="brand__dot"></span>DJ Kestro</div>
</section>

<section class="card card--back" aria-label="Card back">
  <div class="brand brand--back"><span class="brand__dot"></span>DJ Kestro</div>
  <p class="tagline">Offers professional mobile DJ SERVICES including:</p>
  <ul class="services">
    <li>DJ,</li>
    <li>MC,</li>
    <li>Karaoke,</li>
    <li>360 Photo Booth</li>
  </ul>
  <div class="partner"><span class="partner__dot"></span>Silent Disco</div>

  <ul class="contact">
    <li>
      <svg viewBox="0 0 24 24" aria-hidden="true">
        <circle cx="12" cy="12" r="12" fill="var(--accent)"/>
        <path d="M8.5 6.5l2 2.2-1.2 1.6c.8 1.7 2 2.9 3.7 3.7l1.6-1.2 2.2 2-1.3 1.9c-3.9-.3-8-4.4-8.3-8.3z" fill="#fff"/>
      </svg>
      (555) 314-7720
    </li>
    <li>
      <svg viewBox="0 0 24 24" aria-hidden="true">
        <circle cx="12" cy="12" r="12" fill="var(--accent)"/>
        <rect x="6.5" y="8" width="11" height="8" rx="1" fill="#fff"/>
        <path d="M6.8 8.4l5.2 4 5.2-4" fill="none" stroke="var(--accent)" stroke-width="1.2"/>
      </svg>
      lenny.corbitt@mailvane.net
    </li>
  </ul>

  <div class="social">
    <div class="social__icons" aria-hidden="true"><span></span><span></span><span></span><span></span></div>
    <p class="social__handle">@DJKestroBPZ</p>
  </div>
</section>

</body>
</html>
```